Harborlight Unity Collective Sponsorship

FULL PROJECT DESCRIPTION PROVIDED IN PDF AND WORD DOC (UPLOADED).

Harborlight Unity Collective is looking for an updated sponsorship package design – included in the shared information is our sponsorship packaged used in 2017, 2018, and 2019.

The mission of Harborlight Unity Collective is to create opportunities for integrating and promoting visibility for the lesbian. gay, bisexual and transgender community; promoting equal rights and diversity through public education and the arts; provide safe opportunities and venues for people to come out with the ability to express and celebrate their sexual identities.

Some images (because of their size) are not allowed to be uploaded... use the following link to access the full library of images, reference documents, and the full outline: https://files.vexorabox.net/shared/7qTmW3zK9-4rbLnYcP2sVdHgE6uJaXf0N?mode=view

Sponsorship packet design details:
Final file type: .pdf and/or .ai/.eps
Orientation: Preferably landscape but not opposed to a portrait design.
Page count: estimated 6 with current content (not opposed to 8 pages)
Size: 8.5”x11”
Full bleed

Images:
Images for this design are shared in a folder “images for use in sponsorship packet” – please feel free to choose them as you see fit and we can make any notes after the first draft.

Creative Reference:
Additionally, provided are a few sponsorship packages that we like and feel that you might be able to take inspiration from – these are in a folder named “sponsorship packets we like”
Updates

I've updated all of the details of this project and would like to have completed asap. Thank you.

Target Market(s)

Primarily our target market is local and regional businesses that are interested in supporting GlowFair through sponsorship or might be interested in advertising opportunities.

Industry/Entity Type

LGBT

Font styles to use
Serif
Sans Serif

Colors

Designer to choose colors to be used in the design.

Requirements
Must have
• All sponsorship details

```html
<!DOCTYPE html>
<html lang="en">
<head>
<meta charset="utf-8">
<title>Harborlight Unity Collective — Sponsorship 2020</title>
<link rel="stylesheet" href="https://fonts.googleapis.com/css2?family=Bebas+Neue&family=Montserrat:wght@400&display=swap">
<style>
  :root {
    --paper: #ffffff;
    --ink: #333333;
    --ink-soft: #4a4a4a;
    --spectrum: linear-gradient(90deg, #f07a62 0%, #f19a57 22%, #f3c24f 42%, #9cc65a 60%, #3fa6b8 78%, #5a62a8 100%);
  }
  * { box-sizing: border-box; margin: 0; padding: 0; }
  html, body {
    width: 1200px; height: 927px; overflow: hidden;
    background: var(--paper);
  }
  .cover {
    position: relative;
    width: 1200px; height: 927px;
    background: var(--paper);
    overflow: hidden;
  }
  .cover__hero {
    position: absolute;
    left: 20px; top: -20px;
    width: 1160px; height: 640px;
    border-radius: 38% 46% 40% 52% / 30% 28% 58% 62%;
    background:
      radial-gradient(ellipse 30% 28% at 88% 10%, rgba(247, 215, 116, 0.85), transparent 70%),
      radial-gradient(ellipse 34% 40% at 72% 34%, rgba(242, 130, 70, 0.85), transparent 72%),
      radial-gradient(ellipse 30% 40% at 52% 30%, rgba(217, 119, 184, 0.75), transparent 72%),
      radial-gradient(ellipse 30% 42% at 28% 46%, rgba(124, 199, 154, 0.75), transparent 72%),
      radial-gradient(ellipse 26% 36% at 12% 70%, rgba(159, 208, 234, 0.7), transparent 72%),
      radial-gradient(ellipse 50% 50% at 50% 50%, rgba(182, 227, 212, 0.35), transparent 80%);
    filter: blur(6px);
  }
  .cover__title {
    position: absolute;
    right: 48px; top: 512px;
    text-align: right;
    font-family: "Bebas Neue", "Oswald", sans-serif;
    font-weight: 400;
    line-height: 1;
  }
  .cover__name {
    display: block;
    font-size: 96px;
    letter-spacing: 1px;
    color: var(--ink);
  }
  .cover__subtitle {
    display: inline-block;
    margin-top: 22px;
    font-size: 98px;
    letter-spacing: 1px;
    background: var(--spectrum);
    -webkit-background-clip: text;
    background-clip: text;
    color: transparent;
  }
  .social {
    position: absolute;
    top: 774px; left: 0; right: 0;
    height: 26px;
    list-style: none;
    font-family: "Montserrat", "Helvetica Neue", sans-serif;
    font-size: 16px;
    color: var(--ink-soft);
    white-space: nowrap;
  }
  .social__item {
    position: absolute;
    display: flex; align-items: center; gap: 8px;
  }
  .social__item--page { left: 600px; }
  .social__item--photo { left: 830px; }
  .social__item--news { left: 1034px; }
  .social__dot {
    width: 20px; height: 20px;
    border-radius: 50%;
    border: 1.6px solid var(--ink);
    flex: none;
  }
</style>
</head>
<body>
  <main class="cover">
    <div class="cover__hero" role="img" aria-label="Watercolour-washed photograph of a columned civic building with a rainbow flag, in teal, pink, orange and yellow tones"></div>

    <h1 class="cover__title">
      <span class="cover__name">Harborlight Unity Collective</span>
      <span class="cover__subtitle">Sponsorship 2020</span>
    </h1>

    <ul class="social">
      <li class="social__item social__item--page"><span class="social__dot"></span>hub.page/HLUnity</li>
      <li class="social__item social__item--photo"><span class="social__dot"></span>@hl_unity</li>
      <li class="social__item social__item--news"><span class="social__dot"></span>@Unity_HL</li>
    </ul>
  </main>
</body>
</html>
```